Local snack brand needs a WordPress theme design

We need a custom WordPress theme for a new Australian snack company called Crunchwell. Based in Palm Bay, we create functional food snacks using local bananas and other produce. The theme should reflect our community-first philosophy and local roots, featuring an aerial banner of the region’s banana plantations and images of growers harvesting bananas.
The design should include layouts for:
1. Bio pages (profile photo and blurb)
2. Product pages (packaging, nutrition information panel, ingredients, 3. product description, health claim badges like “source of fibre” and “good source of potassium,” and awards)
4. Where to Buy page (interactive map, market stall imagery)
5. Blog posts (feature image, paragraph, quotes)
The final theme should use Crunchwell’s vector logo in the header (without text), and Crunchwell name (in brand font) in the footer. Should be modern, responsive design (mobile first). It should have a grass roots feel, be clean and feel good, leverage the brand colours, but still feel professional (to reflect a horticulturist and nutritionist), and be flexible for future updates. The successful design needs to be delivered as an installable theme in ZIP archive.
Please visit our website and read our pages to get a feel for "us". See https://crunchwell-example.au/
1 week extension for the 3 finalists to respond to feedback and make their final submissions before awarding 1st, 2nd and 3rd.
Local, health-conscious, athletes, busy parents, active minds
Food wholesaler, health & nutrition, agribusiness / local produce
- Galano Grotesque Bold

```html
<!DOCTYPE html>
<html lang="en">
<head>
<meta charset="utf-8">
<title>Crunchwell – Home</title>
<link rel="stylesheet" href="https://fonts.googleapis.com/css2?family=Poppins:wght@400;500;600;700;800&display=swap">
<style>
:root{
  --green:#5d9a30;
  --green-head:#6b9b36;
  --green-dark:#2f4a22;
  --green-deep:#243a1b;
  --green-light:#e7efdb;
  --ink:#161616;
  --text:#333;
  --muted:#777;
  --white:#fff;
  --gold:#d8a417;
  --orange:#c74b1c;
  --berry:#3d5cb8;
  --line:#e3e3e3;
}
*{box-sizing:border-box;margin:0;padding:0}
html,body{width:1200px;height:4098px;overflow:hidden}
body{font-family:"Poppins",sans-serif;color:var(--text);background:var(--white);position:relative}
.abs{position:absolute}
section,header,footer{position:relative;width:1200px;overflow:hidden}
.btn{position:absolute;display:flex;align-items:center;justify-content:center;border-radius:20px;font-weight:700;font-size:11px;letter-spacing:.3px;text-transform:uppercase;color:var(--white)}
.btn-dark{background:var(--ink)}
.btn-green{background:var(--green)}
.section-title{position:absolute;left:0;width:1200px;text-align:center;font-weight:800;font-size:31px;line-height:40px;letter-spacing:.5px;text-transform:uppercase}
.title-flourish{position:absolute;left:580px;width:40px;height:12px}
.brush{position:absolute;left:0;width:1200px;height:8px;background:var(--green);border-radius:4px}
.placeholder{position:absolute}
.banana{position:absolute;background:linear-gradient(135deg,#f7e08a,#e9bf3c);border-radius:50% 50% 50% 50%/60% 60% 40% 40%}

/* header */
.site-header{height:77px;background:var(--white)}
.brand{position:absolute;left:156px;top:26px;display:flex;align-items:center;gap:8px;font-weight:800;font-size:15px;line-height:24px;color:var(--ink);letter-spacing:.3px;text-transform:uppercase}
.brand-dot{width:22px;height:22px;border-radius:50%;background:var(--green)}
.main-nav{position:absolute;left:379px;top:31px;display:flex;gap:25px;font-size:11px;line-height:16px;font-weight:500;text-transform:uppercase;color:var(--ink)}
.main-nav .active{color:var(--green);text-decoration:underline}
.icon-btn{position:absolute;top:24px;width:30px;height:30px;border-radius:50%;background:#ececec;display:flex;align-items:center;justify-content:center}

/* hero */
.hero{height:512px}
.hero-overlay{position:absolute;inset:0;background:rgba(20,15,5,.35)}
.hero-eyebrow{top:165px;left:0;width:1200px;text-align:center;font-size:16px;line-height:22px;font-weight:600;color:var(--white)}
.hero-title{top:186px;left:0;width:1200px;text-align:center;font-size:52px;line-height:62px;font-weight:800;color:var(--white);letter-spacing:1px}
.hero-sub{top:253px;left:400px;width:400px;text-align:center;font-size:12px;line-height:18px;color:var(--white)}

/* story */
.story{height:474px}
.story-title{left:200px;top:108px;font-size:30px;line-height:40px;font-weight:800;color:var(--green-head)}
.story-lead{left:200px;top:167px;width:370px;font-size:11px;font-weight:700;line-height:18px;color:var(--ink)}
.story-body{left:200px;top:217px;width:370px;font-size:11px;line-height:18px;color:var(--text)}
.story-mark{left:688px;top:76px;width:304px;height:325px;display:flex;align-items:center;justify-content:center}
.story-mark .circle{width:300px;height:300px;border-radius:50%;background:var(--green-light);display:flex;align-items:center;justify-content:center;font-weight:800;font-size:34px;color:var(--green)}

/* products */
.products{height:619px;background:linear-gradient(160deg,#4a5a3a,#2e3b25 55%,#3d4a2e)}
.products .section-title{top:66px;color:var(--white)}
.product-card{position:absolute;top:147px;width:250px;height:331px;background:var(--white);text-align:center}
.pack{position:absolute;left:50px;top:30px;width:150px;height:205px;border-radius:8px}
.product-name{position:absolute;top:256px;width:100%;font-size:16px;line-height:22px;font-weight:800;text-transform:uppercase}
.product-desc{position:absolute;top:282px;width:100%;font-size:12.5px;line-height:18px;color:var(--ink)}
.arrow{position:absolute;top:297px;width:34px;height:34px;border-radius:50%;background:rgba(90,140,45,.55);display:flex;align-items:center;justify-content:center}

/* where to buy */
.where{height:430px;background:var(--green-light)}
.where .section-title{top:72px;color:var(--green-head)}
.map-box{left:156px;top:143px;width:372px;height:211px;border:1px solid var(--green);background:linear-gradient(90deg,#d8dad6 0%,#a8e3b4 35%,#a9dcea 75%,#d9dcdc 100%)}
.market-panel{left:528px;top:143px;width:257px;height:211px;background:#3a3a3a;text-align:center;color:var(--white)}
.market-name{position:absolute;top:110px;width:100%;font-size:13px;line-height:18px;font-weight:700;color:#7fb84b}
.market-info{position:absolute;top:133px;width:100%;font-size:11px;line-height:19px}
.where-copy{left:826px;top:164px;width:210px;font-size:11px;line-height:18px;color:var(--ink)}
.where-copy strong{display:block;margin-bottom:10px}

/* ingredients */
.ingredients{height:692px}
.ingredients .section-title{top:62px;color:var(--green-head)}
.ing-tagline{top:143px;left:0;width:1200px;text-align:center;font-size:11px;line-height:16px;font-weight:700;color:var(--ink)}
.ing-intro{top:164px;left:225px;width:750px;text-align:center;font-size:11px;line-height:18px;color:var(--ink)}
.ing-photo-main{left:156px;top:221px;width:337px;height:393px;background:linear-gradient(160deg,#e9f0f3,#6e9bb7 55%,#1e4e73)}
.ing-photo-side{left:364px;top:321px;width:198px;height:204px;border:5px solid var(--white);background:linear-gradient(135deg,#f6d36b,#e8a63a)}
.acc{position:absolute;left:613px;width:429px;border-top:1px solid var(--line)}
.acc-icon{position:absolute;left:18px;width:30px;height:30px;border-radius:50%}
.acc-name{position:absolute;left:68px;font-size:15px;line-height:20px;font-weight:800;text-transform:uppercase}
.acc-sub{position:absolute;left:68px;font-size:11px;line-height:16px;color:var(--ink)}
.acc-detail{position:absolute;left:68px;width:300px;font-size:9px;line-height:13px;color:var(--muted)}
.acc-toggle{position:absolute;right:14px;width:22px;height:22px;border-radius:50%;background:#eee;display:flex;align-items:center;justify-content:center}
.acc-toggle.open{background:var(--green)}

/* blogs */
.blogs{height:535px;background:linear-gradient(160deg,#2f4a22,#233a18 55%,#35502a)}
.blogs .section-title{top:76px;color:var(--white)}
.blog-card{position:absolute;top:159px;width:335px}
.blog-image{height:185px}
.blog-date{position:absolute;left:12px;top:175px;height:22px;padding:0 11px;background:var(--green);color:var(--white);font-size:10px;display:flex;align-items:center;gap:6px}
.blog-excerpt{position:absolute;left:12px;top:218px;width:300px;font-size:12px;line-height:18px;color:var(--white)}

/* inquiry */
.inquiry{height:481px}
.inquiry .section-title{top:74px;color:var(--green-head)}
.field{position:absolute;border:1px solid #ddd;background:var(--white);font-size:9px;line-height:12px;color:#999;padding:11px 12px}

/* footer */
.site-footer{height:246px;background:linear-gradient(160deg,#2b3a24,#1f2b1a 60%,#2d3a25)}
.footer-brand{left:156px;top:108px;display:flex;align-items:center;gap:8px;font-weight:800;font-size:20px;line-height:28px;color:var(--white);text-transform:uppercase}
.footer-brand .brand-dot{width:26px;height:26px}
.footer-col h4{font-size:12px;line-height:16px;font-weight:700;color:#7fb84b;margin-bottom:14px}
.footer-col li{list-style:none;font-size:11px;color:var(--white);line-height:20px}
.contact-row{display:flex;gap:8px;font-size:11px;color:var(--white);line-height:15px;margin-bottom:10px}
.footer-map{left:794px;top:52px;width:250px;height:132px;background:linear-gradient(135deg,#e9ecef,#dde5d6 50%,#e7eaef)}
.bottom-bar{height:32px;background:var(--green);display:flex;align-items:center;color:var(--white);font-size:10px}
.social{position:absolute;top:10px;width:13px;height:13px;background:var(--white);border-radius:3px}
</style>
</head>
<body>

<header class="site-header">
  <div class="brand"><span class="brand-dot"></span>Crunchwell</div>
  <nav class="main-nav">
    <span class="active">Home</span><span>Our Story</span><span>Products</span><span>Where To Buy</span><span>Contact Us</span>
  </nav>
  <div class="icon-btn" style="left:835px">
    <svg width="12" height="12" viewBox="0 0 24 24"><path d="M6.6 10.8a15 15 0 0 0 6.6 6.6l2.2-2.2a1 1 0 0 1 1-.25 11 11 0 0 0 3.6.6 1 1 0 0 1 1 1V20a1 1 0 0 1-1 1A17 17 0 0 1 3 4a1 1 0 0 1 1-1h3.5a1 1 0 0 1 1 1 11 11 0 0 0 .6 3.6 1 1 0 0 1-.25 1z" fill="#222"/></svg>
  </div>
  <div class="icon-btn" style="left:872px">
    <svg width="12" height="12" viewBox="0 0 24 24"><path d="M3 5h18v14H3z" fill="#222"/><path d="M3 5l9 7 9-7" stroke="#ececec" stroke-width="2" fill="none"/></svg>
  </div>
  <div class="btn btn-dark" style="left:920px;top:23px;width:124px;height:32px">Quick Inquiry</div>
</header>

<section class="hero">
  <div class="placeholder" role="img" aria-label="Plate of golden banana chips on a kitchen table" style="inset:0;background:radial-gradient(ellipse at 50% 75%,#c9922e 0%,#8a6a2e 45%,#5b4a28 100%)"></div>
  <div class="hero-overlay"></div>
  <div class="abs hero-eyebrow">WELCOME TO</div>
  <div class="abs hero-title">CRUNCHWELL</div>
  <p class="abs hero-sub">The science of functional snacking - grown, crafted and shared on the Palm Coast.</p>
  <div class="btn btn-green" style="left:546px;top:311px;width:142px;height:32px">Contact Now</div>
  <div class="brush" style="bottom:0"></div>
</section>

<section class="story">
  <div class="banana" role="img" aria-label="Banana chip" style="left:1046px;top:60px;width:106px;height:70px;transform:rotate(20deg)"></div>
  <div class="banana" role="img" aria-label="Banana chip" style="left:29px;top:318px;width:115px;height:64px;transform:rotate(-12deg)"></div>
  <h2 class="abs story-title">OUR STORY</h2>
  <p class="abs story-lead">We're Sam &amp; Jordan - two locals passionate about real food, good soil, and better snacks.</p>
  <p class="abs story-body">Crunchwell began as a conversation between a horticulturist and a nutritionist - a grower and a formulator - about how much perfectly good produce never makes it to people's plates, and how much better snacking could be if we treated it with the same respect we give meals.</p>
  <div class="btn btn-dark" style="left:200px;top:334px;width:106px;height:30px">Read More</div>
  <div class="abs story-mark"><div class="circle">Crunchwell</div></div>
</section>

<section class="products">
  <div class="brush" style="top:0"></div>
  <h2 class="section-title">Products</h2>
  <svg class="title-flourish" style="top:106px" viewBox="0 0 40 12"><path d="M2 6 Q14 2 30 6" stroke="#fff" stroke-width="1.5" fill="none"/><circle cx="34" cy="6" r="3" fill="none" stroke="#fff" stroke-width="1.5"/></svg>
  <div class="arrow" style="left:144px"><svg width="10" height="10" viewBox="0 0 10 10"><path d="M7 1 3 5l4 4" stroke="#fff" stroke-width="1.6" fill="none"/></svg></div>
  <div class="arrow" style="left:1020px"><svg width="10" height="10" viewBox="0 0 10 10"><path d="M3 1l4 4-4 4" stroke="#fff" stroke-width="1.6" fill="none"/></svg></div>

  <div class="product-card" style="left:200px">
    <div class="pack" role="img" aria-label="Green snack pack with banana and coconut chips" style="background:linear-gradient(180deg,#1f6b3a,#2e8a45 60%,#3aa04f)"></div>
    <div class="product-name" style="color:#4f9a2e">Cocobite</div>
    <div class="product-desc">Banana + Desiccated Coconut</div>
  </div>
  <div class="product-card" style="left:476px">
    <div class="pack" role="img" aria-label="Olive snack pack with cinnamon banana chips" style="background:linear-gradient(180deg,#7a6a1f,#9a842a 60%,#b3972f)"></div>
    <div class="product-name" style="color:#8a7a16">Cinnacrunch</div>
    <div class="product-desc">Banana + Cinnamon</div>
  </div>
  <div class="product-card" style="left:750px">
    <div class="pack" role="img" aria-label="Red snack pack with banana coffee bites" style="background:linear-gradient(180deg,#8a1f1a,#a8341c 60%,#c9561f)"></div>
    <div class="product-name" style="color:var(--orange)">Mochabite</div>
    <div class="product-desc">Banana + Ground Coffee</div>
  </div>
  <div class="btn btn-green" style="left:547px;top:511px;width:106px;height:32px">View All</div>
  <div class="brush" style="bottom:0"></div>
</section>

<section class="where">
  <div class="banana" role="img" aria-label="Banana chip" style="left:-10px;top:64px;width:92px;height:58px;transform:rotate(-18deg)"></div>
  <h2 class="section-title">Where To Buy</h2>
  <svg class="title-flourish" style="top:116px" viewBox="0 0 40 12"><path d="M2 6 Q14 2 30 6" stroke="#5d9a30" stroke-width="1.5" fill="none"/><circle cx="34" cy="6" r="3" fill="none" stroke="#5d9a30" stroke-width="1.5"/></svg>
  <div class="abs map-box" role="img" aria-label="Street map of the harbour foreshore showing the market location"></div>
  <div class="abs market-panel">
    <svg class="abs" style="left:103px;top:42px" width="50" height="54" viewBox="0 0 50 54">
      <path d="M20 2a17 17 0 0 1 17 17c0 13-17 31-17 31S3 32 3 19A17 17 0 0 1 20 2z" fill="#6aa63a"/>
      <circle cx="20" cy="19" r="6" fill="#3a3a3a"/>
      <circle cx="36" cy="37" r="10" fill="#fff"/>
      <path d="M36 31v6h5" stroke="#3a3a3a" stroke-width="2" fill="none"/>
    </svg>
    <div class="market-name">Seaside Growers Market</div>
    <div class="market-info">Pier Foreshore, Palm Bay<br>Every Saturday, 7am–1pm</div>
  </div>
  <div class="abs where-copy">
    <strong>Find us by the beach every Saturday</strong>
    You can catch Crunchwell in person every week at the Seaside Growers Market - a beautiful makers and growers market held at the Pier Foreshore in Palm Bay.
  </div>
  <div class="btn btn-dark" style="left:826px;top:322px;width:105px;height:30px">Read More</div>
</section>

<section class="ingredients">
  <div class="banana" role="img" aria-label="Banana chip" style="left:1088px;top:124px;width:100px;height:62px;transform:rotate(-25deg)"></div>
  <div class="banana" role="img" aria-label="Banana chip" style="left:-20px;top:300px;width:125px;height:170px;transform:rotate(8deg)"></div>
  <h2 class="section-title">Our Ingredients</h2>
  <svg class="title-flourish" style="top:106px" viewBox="0 0 40 12"><path d="M2 6 Q14 2 30 6" stroke="#5d9a30" stroke-width="1.5" fill="none"/><circle cx="34" cy="6" r="3" fill="none" stroke="#5d9a30" stroke-width="1.5"/></svg>
  <p class="abs ing-tagline">Thoughtfully sourced. Naturally nutritious. Made to fuel better.</p>
  <p class="abs ing-intro">At Crunchwell, what goes into our snacks matters as much as what doesn't. Every batch we make starts with real, whole ingredients, sourced as close to home as possible and chosen for their nutritional value, flavour, and sustainability. <strong>Read More</strong></p>
  <div class="abs ing-photo-main" role="img" aria-label="Split coconut splashing into water"></div>
  <div class="abs ing-photo-side" role="img" aria-label="Pile of crisp banana chips"></div>

  <div class="acc" style="top:240px;height:61px">
    <div class="acc-icon" style="top:16px;background:#f2c933"></div>
    <div class="acc-name" style="top:11px;color:var(--gold)">Bananas</div>
    <div class="acc-sub" style="top:33px">Local, Naturally Sweet</div>
    <div class="acc-toggle" style="top:19px"><svg width="8" height="8" viewBox="0 0 8 8"><path d="M1 2.5 4 5.5 7 2.5" stroke="#333" fill="none"/></svg></div>
  </div>
  <div class="acc" style="top:301px;height:135px">
    <div class="acc-icon" style="top:14px;background:#8a5a36"></div>
    <div class="acc-name" style="top:10px;color:var(--orange);font-size:14px">Coconut</div>
    <div class="acc-sub" style="top:30px">A Tropical Partner</div>
    <div class="acc-detail" style="top:53px">We Use Desiccated Coconut To Add Texture And A Creamy Sweetness To Blends Like Our Signature Cocobite.</div>
    <div class="acc-detail" style="top:86px">Our Coconut Is Carefully Selected For Purity And Minimal Processing, Keeping It As Close To The Source As Possible. It Adds Good Fats, Fibre, And Flavour To Our Snacks.</div>
    <div class="acc-toggle open" style="top:16px"><svg width="8" height="8" viewBox="0 0 8 8"><path d="M1 5.5 4 2.5 7 5.5" stroke="#fff" fill="none"/></svg></div>
  </div>
  <div class="acc" style="top:436px;height:56px">
    <div class="acc-icon" style="top:13px;background:#d9a440"></div>
    <div class="acc-name" style="top:10px;color:var(--gold);font-size:13px">Macadamias</div>
    <div class="acc-sub" style="top:28px">Grown In The Northern Hills</div>
    <div class="acc-toggle" style="top:16px"><svg width="8" height="8" viewBox="0 0 8 8"><path d="M1 2.5 4 5.5 7 2.5" stroke="#333" fill="none"/></svg></div>
  </div>
  <div class="acc" style="top:492px;height:55px;border-bottom:1px solid var(--line)">
    <div class="acc-icon" style="top:13px;background:#4a63c8"></div>
    <div class="acc-name" style="top:10px;color:var(--berry);font-size:13px">Berries</div>
    <div class="acc-sub" style="top:28px">Blueberries And More</div>
    <div class="acc-toggle" style="top:16px"><svg width="8" height="8" viewBox="0 0 8 8"><path d="M1 2.5 4 5.5 7 2.5" stroke="#333" fill="none"/></svg></div>
  </div>
  <div class="btn btn-dark" style="left:613px;top:572px;width:90px;height:30px">View All</div>
</section>

<section class="blogs">
  <div class="brush" style="top:0"></div>
  <h2 class="section-title">Our Blogs</h2>
  <svg class="title-flourish" style="top:120px" viewBox="0 0 40 12"><path d="M2 6 Q14 2 30 6" stroke="#fff" stroke-width="1.5" fill="none"/><circle cx="34" cy="6" r="3" fill="none" stroke="#fff" stroke-width="1.5"/></svg>
  <article class="blog-card" style="left:251px">
    <div class="blog-image" role="img" aria-label="Wooden bowl of banana chips" style="background:linear-gradient(135deg,#b9b3a8,#d9b46a 50%,#6a4a2a)"></div>
    <div class="blog-date"><svg width="10" height="10" viewBox="0 0 10 10"><rect x="1" y="2" width="8" height="7" fill="none" stroke="#fff"/><path d="M1 4h8" stroke="#fff"/></svg>Aug 26, 2025</div>
    <p class="blog-excerpt">Lorem Ipsum Is Simply Dummy Text Of The Printing And Typesetting Industry...</p>
  </article>
  <article class="blog-card" style="left:614px">
    <div class="blog-image" role="img" aria-label="Ridged chips beside a bowl of tomato dip" style="background:linear-gradient(90deg,#f0d068,#e8c050 55%,#c0392b 85%,#e8e4de)"></div>
    <div class="blog-date"><svg width="10" height="10" viewBox="0 0 10 10"><rect x="1" y="2" width="8" height="7" fill="none" stroke="#fff"/><path d="M1 4h8" stroke="#fff"/></svg>Aug 26, 2025</div>
    <p class="blog-excerpt">Lorem Ipsum Is Simply Dummy Text Of The Printing And Typesetting Industry...</p>
  </article>
  <div class="btn btn-dark" style="left:555px;top:432px;width:90px;height:30px">View All</div>
  <div class="brush" style="bottom:0"></div>
</section>

<section class="inquiry">
  <div class="banana" role="img" aria-label="Dried banana slices" style="left:20px;top:90px;width:118px;height:110px;border-radius:45%"></div>
  <div class="banana" role="img" aria-label="Banana chip" style="left:150px;top:330px;width:125px;height:95px;transform:rotate(25deg)"></div>
  <div class="banana" role="img" aria-label="Banana chip" style="left:1040px;top:150px;width:160px;height:110px;transform:rotate(-10deg)"></div>
  <h2 class="section-title">Quick Inquiry</h2>
  <svg class="title-flourish" style="top:118px" viewBox="0 0 40 12"><path d="M2 6 Q14 2 30 6" stroke="#5d9a30" stroke-width="1.5" fill="none"/><circle cx="34" cy="6" r="3" fill="#5d9a30"/></svg>
  <div class="field" style="left:325px;top:156px;width:269px;height:33px">First Name</div>
  <div class="field" style="left:606px;top:156px;width:269px;height:33px">Last Name</div>
  <div class="field" style="left:325px;top:205px;width:269px;height:33px">Email</div>
  <div class="field" style="left:606px;top:205px;width:269px;height:33px">Phone</div>
  <div class="field" style="left:325px;top:255px;width:550px;height:78px">How Can We Help?</div>
  <div class="btn btn-dark" style="left:559px;top:366px;width:82px;height:30px">Submit</div>
  <div class="brush" style="bottom:0"></div>
</section>

<footer class="site-footer">
  <div class="abs footer-brand"><span class="brand-dot"></span>Crunchwell</div>
  <div class="abs footer-col" style="left:395px;top:66px">
    <h4>Contact Us</h4>
    <div class="contact-row"><svg width="10" height="10" viewBox="0 0 24 24"><path d="M6.6 10.8a15 15 0 0 0 6.6 6.6l2.2-2.2a1 1 0 0 1 1-.25 11 11 0 0 0 3.6.6 1 1 0 0 1 1 1V20a1 1 0 0 1-1 1A17 17 0 0 1 3 4a1 1 0 0 1 1-1h3.5a1 1 0 0 1 1 1 11 11 0 0 0 .6 3.6 1 1 0 0 1-.25 1z" fill="#7fb84b"/></svg>+1 555-014-0025</div>
    <div class="contact-row"><svg width="10" height="10" viewBox="0 0 24 24"><path d="M3 5h18v14H3z" fill="#7fb84b"/></svg>info@crunchwell-example.au</div>
    <div class="contact-row"><svg width="10" height="12" viewBox="0 0 24 28"><path d="M12 1a10 10 0 0 1 10 10c0 8-10 16-10 16S2 19 2 11A10 10 0 0 1 12 1z" fill="#7fb84b"/></svg><span>20 Sample Street,<br>Springfield, ST 10003</span></div>
  </div>
  <div class="abs footer-col" style="left:629px;top:66px">
    <h4>Quick Links</h4>
    <ul><li style="color:#7fb84b;text-decoration:underline">Home</li><li>Our Story</li><li>Products</li><li>Where To Buy</li><li>Contact Us</li></ul>
  </div>
  <div class="abs footer-map" role="img" aria-label="Regional map showing the business location"></div>
</footer>

<div class="bottom-bar" style="position:relative;width:1200px">
  <span class="abs" style="left:156px">© 2025 Crunchwell – All Rights Reserved. &nbsp;&nbsp;&nbsp;&nbsp; Privacy Policy</span>
  <span class="social" style="left:966px"></span>
  <span class="social" style="left:994px"></span>
  <span class="social" style="left:1024px;width:16px;height:16px;top:8px;border-radius:50%"></span>
</div>

</body>
</html>
```